Realtor Business Card

To create a new cutting edge classic 2-sided business card. Including personal logo, company logo, and contact info. Possibly including a headshot and slogon.
"4 Generations of Victoria Real Estate Service"
The company's color is dark blue. My logo color is green as indicated on the attached files.
Company logos on one side (Thornbury Realty and Ashgrove Home Estate) personal info and logo on the other.

```html
<!DOCTYPE html>
<html lang="en">
<head>
<meta charset="utf-8">
<title>Dean Calloway – Business Card</title>
<link href="https://fonts.googleapis.com/css2?family=Cinzel:wght@400;500&family=Roboto:wght@400;500&family=Roboto+Condensed:wght@400&display=swap" rel="stylesheet">
<style>
  :root {
    --backdrop: #5a524d;
    --card: #343434;
    --gold: #b9a77a;
    --white: #f4f2ee;
    --ink: #2e2e2e;
    --photo-warm: #94614a;
    --photo-brown: #6e4636;
    --photo-suit: #2c2e38;
    --photo-shirt: #d9d6d2;
  }
  * { box-sizing: border-box; margin: 0; padding: 0; }
  html, body { width: 1200px; height: 801px; overflow: hidden; }
  body {
    background: var(--backdrop);
    position: relative;
    font-family: "Roboto", sans-serif;
  }
  .card {
    position: absolute;
    top: 70px;
    width: 380px;
    height: 660px;
    background: var(--card);
    box-shadow: 0 10px 30px rgba(0,0,0,.35);
    overflow: hidden;
  }
  .card--info { left: 170px; }
  .card--portrait { left: 650px; }

  /* company names */
  .brand {
    position: absolute;
    left: 0; right: 0;
    display: flex;
    align-items: center;
    justify-content: center;
    gap: 10px;
    color: var(--gold);
    font-family: "Cinzel", serif;
    font-weight: 500;
  }
  .brand__square { width: 16px; height: 16px; background: var(--gold); flex: none; }
  .brand--company { top: 70px; font-size: 24px; }
  .brand--partner { top: 118px; font-size: 18px; letter-spacing: 1px; }

  .agent-name {
    position: absolute;
    left: 58px;
    top: 292px;
    font-family: "Cinzel", serif;
    font-weight: 500;
    line-height: 1;
  }
  .agent-name__first { color: var(--white); font-size: 58px; display: block; }
  .agent-name__last { color: var(--gold); font-size: 52px; display: block; margin-top: 4px; }

  .title-band {
    position: absolute;
    left: 0;
    width: 340px;
    top: 438px;
    height: 74px;
    background: var(--gold);
    padding: 13px 0 0 58px;
    font-family: "Roboto Condensed", sans-serif;
    color: var(--ink);
    font-size: 18px;
    letter-spacing: 2px;
    line-height: 1.2;
  }

  .contact {
    position: absolute;
    left: 42px;
    display: flex;
    align-items: flex-start;
    gap: 22px;
    color: var(--white);
    font-size: 17px;
    line-height: 1.35;
  }
  .contact svg { flex: none; margin-top: 2px; }
  .contact--phone { top: 532px; }
  .contact--web { top: 592px; }

  /* portrait side */
  .headshot {
    position: absolute;
    inset: 0 0 130px 0;
    background:
      radial-gradient(ellipse 30% 22% at 62% 72%, rgba(217,214,210,.55), rgba(217,214,210,0) 100%),
      radial-gradient(ellipse 55% 35% at 50% 30%, rgba(148,97,74,.9), rgba(148,97,74,0) 100%),
      linear-gradient(to bottom,
        var(--photo-brown) 0%,
        var(--photo-warm) 30%,
        var(--photo-brown) 52%,
        var(--photo-suit) 68%,
        var(--photo-suit) 86%,
        var(--card) 100%);
  }
  .signature {
    position: absolute;
    left: 34px;
    right: 24px;
    bottom: 62px;
    display: flex;
    align-items: center;
    gap: 16px;
  }
  .signature__square {
    width: 58px; height: 58px;
    background: var(--gold);
    border-radius: 6px;
    flex: none;
  }
  .signature__name {
    font-family: "Cinzel", serif;
    font-weight: 500;
    color: var(--gold);
    font-size: 27px;
    border-bottom: 1px solid var(--gold);
    padding-bottom: 4px;
    white-space: nowrap;
  }
  .signature__role {
    font-family: "Roboto Condensed", sans-serif;
    color: var(--gold);
    font-size: 10.5px;
    letter-spacing: 1px;
    margin-top: 5px;
    white-space: nowrap;
  }
</style>
</head>
<body>

<section class="card card--info">
  <div class="brand brand--company"><span class="brand__square"></span>Thornbury Realty</div>
  <div class="brand brand--partner">Ashgrove Home Estate</div>

  <h1 class="agent-name">
    <span class="agent-name__first">Dean</span>
    <span class="agent-name__last">Calloway</span>
  </h1>

  <div class="title-band">REAL ESTATE PROFESSIONAL<br>VICTORIA, BC</div>

  <div class="contact contact--phone">
    <svg width="26" height="38" viewBox="0 0 26 38" aria-hidden="true">
      <rect x="2" y="2" width="22" height="34" rx="3" fill="none" stroke="var(--gold)" stroke-width="2.5"/>
      <line x1="10" y1="31" x2="16" y2="31" stroke="var(--gold)" stroke-width="2"/>
    </svg>
    <p>250-555-0142 Cell<br>250-555-0187 Office</p>
  </div>

  <div class="contact contact--web">
    <svg width="26" height="30" viewBox="0 0 30 30" aria-hidden="true">
      <circle cx="15" cy="15" r="12" fill="none" stroke="var(--gold)" stroke-width="2.5"/>
      <path d="M14 13 L24 17 L19 19 L17 24 Z" fill="var(--gold)"/>
    </svg>
    <p>dean@callowayhomes.ca<br>www.callowayhomes.ca</p>
  </div>
</section>

<section class="card card--portrait">
  <div class="headshot" role="img" aria-label="Headshot of the agent in a dark blazer and white open-collar shirt against a warm brown backdrop"></div>
  <div class="signature">
    <span class="signature__square"></span>
    <div>
      <div class="signature__name">Dean Calloway</div>
      <div class="signature__role">REAL ESTATE PROFESSIONAL - VICTORIA, BC</div>
    </div>
  </div>
</section>

</body>
</html>
```